Luftpolster-Versandtaschen  designen
Luftpolster-Versandtaschen designen
Zielgruppe
Es ist eine natürliche Schmerzsalbe entwickelt und hergestellt in Deutschland.
Die MONDA Salbe gibt ein zuverlässige Gefühl, durch ein innovatives Naturprodukt erstaunlich schnelle, wirkungsvolle Hilfe bei Schmerzen des Bewegungsapparates und bei Hautschäden zu erhalten und dabei gleichzeitig die Haut zu pflegen.
Aufgabenstellung
Wir möchten unsere Luftpolster-Versandtaschen gestalten lassen und das Corporate Design dort platzieren.
Ziel soll sein, das der Kunde eine hohe Aufmerksamkeit schon, vor dem Öffnen und das Vertrauen erhöht, schnelle Wiedererkennung der Marke Monda Kräuterbalsam.
Die Druckdateien benötigen wir als pdf oder jedwede andere Datei mit einer Mindestauflösung von 300 dpi. Die Farbdarstellung erfolgt in CMYK. Alle Grafiken werden mittig platziert und proportional angepasst. Die genauen Maße der Versandtaschen bitte den Dokument vorlage_packbag entnehmen.
Farben / Texte / Bilder können von den Dokument (neue_webseite_alle_seiten_uebersicht) verwendet werden.
Bitte die Datei (vorlage_packbag_14d.pdf) von der Druckerei beachten.

```html
<!DOCTYPE html>
<html lang="de">
<head>
<meta charset="utf-8">
<title>Silber Monda – Versandtasche</title>
<link href="https://fonts.googleapis.com/css2?family=Open+Sans:ital,wght@0,400;0,600;0,700;0,800;1,400&display=swap" rel="stylesheet">
<style>
  :root {
    --backdrop: #ececec;
    --bag: #ffffff;
    --ink: #1c1c1c;
    --grey-text: #8a8a8a;
    --orange-light: #f1b866;
    --orange-mid: #eba544;
    --orange-deep: #e8702a;
    --cream: #f7efe2;
    --icon-fill: #eebd72;
  }
  * { box-sizing: border-box; margin: 0; padding: 0; }
  html, body {
    width: 1200px; height: 877px; overflow: hidden;
    background: var(--backdrop);
    font-family: "Open Sans", Arial, sans-serif;
  }
  .canvas {
    position: relative; width: 1200px; height: 877px;
    display: flex; justify-content: center; align-items: center;
  }
  .mailer {
    position: relative;
    width: 580px; height: 830px;
    background: var(--bag);
    box-shadow: 0 6px 24px rgba(0,0,0,0.08);
    display: flex; flex-direction: column; align-items: center;
  }
  .brand {
    margin-top: 120px;
    display: flex; flex-direction: column; align-items: center;
  }
  .brand-row { display: flex; align-items: center; gap: 12px; }
  .brand-dot {
    width: 34px; height: 34px; border-radius: 50%;
    background: var(--orange-mid);
  }
  .brand-name {
    font-weight: 800; font-size: 44px; color: var(--ink);
    letter-spacing: 1px; line-height: 1;
  }
  .brand-line {
    margin-top: 10px;
    font-weight: 600; font-size: 13px; letter-spacing: 1.5px;
    color: var(--orange-mid);
  }
  .hero {
    margin-top: 70px;
    width: 300px; height: 300px;
    background: linear-gradient(135deg, var(--orange-light) 0%, var(--orange-mid) 55%, var(--orange-light) 100%);
    display: flex; flex-direction: column; justify-content: center;
    padding-left: 34px;
  }
  .hero-title {
    font-weight: 800; font-size: 40px; line-height: 1.05;
    color: var(--orange-deep); letter-spacing: 4px;
  }
  .hero-title .spaced { letter-spacing: 14px; }
  .hero-claim {
    margin-top: 4px;
    font-weight: 800; font-size: 23px; line-height: 1.15;
    color: var(--cream);
  }
  .tagline {
    margin-top: 30px;
    font-style: italic; font-size: 14.5px; letter-spacing: 1.6px;
    color: var(--grey-text);
  }
  .benefits {
    margin-top: 26px;
    width: 500px;
    display: flex; justify-content: space-between; align-items: flex-start;
  }
  .benefit { display: flex; align-items: center; gap: 8px; }
  .benefit:nth-child(2) { margin-top: 22px; }
  .benefit:nth-child(3) { margin-top: 48px; }
  .benefit-icon {
    width: 30px; height: 30px; border-radius: 50%;
    background: var(--icon-fill);
    display: flex; align-items: center; justify-content: center;
  }
  .benefit-label {
    font-weight: 600; font-size: 7.5px; letter-spacing: 0.6px;
    color: var(--grey-text); text-transform: uppercase;
  }
</style>
</head>
<body>
<main class="canvas">
  <section class="mailer">
    <header class="brand">
      <div class="brand-row">
        <span class="brand-dot"></span>
        <span class="brand-name">MONDA</span>
      </div>
      <p class="brand-line">SILBER MONDA</p>
    </header>

    <div class="hero">
      <h1 class="hero-title">SILBER<br><span class="spaced">MONDA!</span></h1>
      <p class="hero-claim">MIT DER KRAFT<br>AUS DER NATUR</p>
    </div>

    <p class="tagline">Hält jung, macht beweglich. Mit der 10-Kräuter-Aktivformel</p>

    <ul class="benefits">
      <li class="benefit">
        <span class="benefit-icon">
          <svg width="18" height="18" viewBox="0 0 18 18" fill="none" stroke="#fff" stroke-width="1.2" stroke-linecap="round" stroke-linejoin="round">
            <path d="M9 2 C7 5 6.5 6.5 6.5 7.5 a2.5 2.5 0 0 0 5 0 C11.5 6.5 11 5 9 2Z"/>
            <path d="M2 12 h4 l3 1.5 h3 l4-2.5"/>
            <path d="M2 15 h4 l4 1 l6-3"/>
          </svg>
        </span>
        <span class="benefit-label">Entspannt und regeneriert</span>
      </li>
      <li class="benefit">
        <span class="benefit-icon">
          <svg width="18" height="18" viewBox="0 0 18 18" fill="none" stroke="#fff" stroke-width="1.2" stroke-linecap="round" stroke-linejoin="round">
            <path d="M9 16 V9"/>
            <path d="M9 9 C9 5 6 3 3 3 C3 7 5 9 9 9Z"/>
            <path d="M9 9 C9 5 12 3 15 3 C15 7 13 9 9 9Z"/>
          </svg>
        </span>
        <span class="benefit-label">100% Natur</span>
      </li>
      <li class="benefit">
        <span class="benefit-icon">
          <svg width="18" height="18" viewBox="0 0 18 18" fill="none" stroke="#fff" stroke-width="1.2" stroke-linecap="round" stroke-linejoin="round">
            <path d="M3 8 h12 c0 4-3 6-6 6 s-6-2-6-6Z"/>
            <path d="M7 14 l-1 2 h6 l-1-2"/>
            <path d="M10 8 L13 2.5"/>
          </svg>
        </span>
        <span class="benefit-label">Stärkt, pflegt, schützt</span>
      </li>
    </ul>
  </section>
</main>
</body>
</html>
```